Book design for Martial Arts Business

TITLE : The Lantern Ledger Method

Subtitle : " Master your business , Master your life

Author Hollis Penwarden

I need a book cover design for my new book which is on Martial Arts Busines Success.

Simple and Powerful Black and red in Design
Strong font , thats clear and easy to read
the Tag line of the book is " Master your business, Master your life ( I want this to stand out )

Front cover image with dojo

Back image of myself

space for 2 endorsement and writing about the book

I dont want it to look cheesy or American must have an uk feel too

No money on the book whatsoever

I have attached a design so far for you to see but want variations
Updates

Reason: Not quite got the look on this we will have to extend this

Need extra days to review

Need extra days to review

Target Market(s)

Martial Arts Business owners

Industry/Entity Type

Business

Colors
000000
ec1f27

Requirements
Must have
• Red and Black in colour
• good font thats not standard .. Impactful and clear
• Images used and any other ideas
Nice to have
• No money in it
Should not have
• Clear and powerful design

```html
<!DOCTYPE html>
<html lang="en">
<head>
<meta charset="utf-8">
<title>The Lantern Ledger Method – Book Cover</title>
<link rel="stylesheet" href="https://fonts.googleapis.com/css2?family=Shojumaru&family=Oswald:wght@500;600&family=Alegreya:wght@400;500&display=swap">
<style>
  :root {
    --ink: #000000;
    --red: #ec1f27;
    --white: #ffffff;
    --panel: rgba(0, 0, 0, 0.62);
    --band: rgba(0, 0, 0, 0.55);
    --body-text: #f2f2f2;
  }
  * { box-sizing: border-box; margin: 0; padding: 0; }
  html, body { width: 1200px; height: 864px; overflow: hidden; background: var(--ink); }
  .cover { position: relative; width: 1200px; height: 864px; overflow: hidden; background: var(--ink); }

  .dojo-photo {
    position: absolute; left: 0; top: 225px; width: 1200px; height: 639px;
    background:
      linear-gradient(180deg, rgba(0,0,0,0.9) 0%, rgba(0,0,0,0) 18%),
      linear-gradient(180deg, #3a3535 0%, #8a8585 22%, #b9b4b4 34%, #7a2a2c 46%, #c92a2f 60%, #a91d22 80%, #5a1214 100%);
  }
  .back-shade {
    position: absolute; left: 0; top: 225px; width: 560px; height: 639px;
    background: linear-gradient(180deg, rgba(0,0,0,0.85) 0%, rgba(0,0,0,0.55) 60%, rgba(0,0,0,0.45) 100%);
  }
  .spine-shade { position: absolute; left: 560px; top: 0; width: 62px; height: 864px; background: rgba(0,0,0,0.45); }

  .title-light { font-family: "Shojumaru", cursive; color: var(--white); line-height: 1; }
  .title-red { font-family: "Shojumaru", cursive; color: var(--red); line-height: 1; }

  .serif-copy { font-family: "Alegreya", serif; font-variant-numeric: oldstyle-nums; color: var(--body-text); }

  /* Back cover */
  .back { position: absolute; left: 0; top: 0; width: 560px; height: 864px; }
  .back .title { position: absolute; top: 34px; width: 100%; text-align: center; }
  .back .title-light { font-size: 34px; }
  .back .title-red { font-size: 44px; margin-top: 8px; }
  .blurb {
    position: absolute; left: 52px; top: 154px; width: 480px;
    font-size: 14.5px; line-height: 19px; text-align: center;
  }
  .endorsements {
    position: absolute; left: 40px; top: 327px; width: 517px; height: 153px;
    background: var(--panel); text-align: center; padding-top: 10px;
  }
  .endorsements h2 { font-weight: 400; font-size: 24px; margin-bottom: 12px; color: var(--white); font-variant-numeric: normal; }
  .endorsements p { font-size: 13.5px; line-height: 17px; margin: 0 30px 14px; }
  .author-bio { position: absolute; left: 40px; top: 494px; width: 517px; height: 212px; background: var(--panel); }
  .author-portrait {
    position: absolute; left: 3px; top: 1px; width: 244px; height: 210px;
    border: 3px solid var(--white);
    background: radial-gradient(ellipse at 50% 40%, #8c8a88 0%, #4a4846 55%, #2a2828 100%);
  }
  .author-bio p {
    position: absolute; left: 260px; top: 16px; width: 250px;
    font-size: 13.5px; line-height: 17.5px;
  }

  /* Spine */
  .spine { position: absolute; left: 562px; top: 0; width: 58px; height: 864px; }
  .spine-title, .spine-author {
    position: absolute; left: 50%; transform: translateX(-50%); writing-mode: vertical-rl; white-space: nowrap;
  }
  .spine-title { top: 28px; font-size: 23px; }
  .spine-author { top: 600px; font-family: "Oswald", sans-serif; font-weight: 600; font-size: 26px; color: var(--white); letter-spacing: 0.5px; }

  /* Front cover */
  .front { position: absolute; left: 620px; top: 0; width: 580px; height: 864px; }
  .front .title { position: absolute; top: 30px; width: 100%; text-align: center; }
  .front .title-light { font-size: 50px; }
  .front .title-red { font-size: 84px; margin-top: 14px; }
  .front .title-red + .title-red { margin-top: 6px; }
  .tagline {
    position: absolute; top: 312px; width: 100%; text-align: center;
    font-family: "Oswald", sans-serif; font-weight: 500; font-size: 25px; color: var(--white); letter-spacing: 0.3px;
  }
  .tagline-glow { position: absolute; left: 90px; top: 348px; }
  .author-band { position: absolute; left: 0; top: 745px; width: 580px; height: 119px; background: var(--band); }
  .author-name {
    position: absolute; top: 762px; width: 100%; text-align: center;
    font-family: "Oswald", sans-serif; font-weight: 600; font-size: 56px; color: var(--white); letter-spacing: 0.5px;
  }
</style>
</head>
<body>
<main class="cover">
  <div class="dojo-photo" role="img" aria-label="Photograph of a dojo interior with red and black floor mats and hanging punch bags"></div>
  <div class="back-shade"></div>
  <div class="spine-shade"></div>

  <section class="back">
    <h1 class="title">
      <div class="title-light">The Lantern</div>
      <div class="title-red">Ledger Method</div>
    </h1>
    <p class="blurb serif-copy">Lorem Ipsum is simply dummy text of the printing and typesetting industry. Lorem Ipsum has been the industry's standard dummy text ever since the 1500s, when an unknown printer took a galley of type and scrambled it to make a type specimen book. It has survived not only five centuries, but also the leap into electronic typesetting, remaining essentially unchanged. It was popularised in the 1960s with the release of Brightmark sheets containing Lorem Ipsum passages, and more recently with desktop publishing software like Foliocraft Studio including versions of Lorem Ipsum.</p>
    <div class="endorsements serif-copy">
      <h2>Testimonial</h2>
      <p>Lorem Ipsum is simply dummy text of the printing and typesetting industry. Lorem Ipsum has been the industry's standard dummy text ever since the 1500s</p>
      <p>Lorem Ipsum is simply dummy text of the printing and typesetting industry. Lorem Ipsum has been the industry's standard dummy text ever since the 1500s</p>
    </div>
    <div class="author-bio">
      <div class="author-portrait" role="img" aria-label="Portrait photograph of the author in a martial arts jacket"></div>
      <p class="serif-copy">Lorem Ipsum is simply dummy text of the printing and typesetting industry. Lorem Ipsum has been the industry's standard dummy text ever since the 1500s, when an unknown printer took a galley of type and scrambled it to make a type specimen book. It has survived not only five centuries, but also the leap into electronic typesetting, remaining essentially unchanged.</p>
    </div>
  </section>

  <section class="spine">
    <div class="spine-title"><span class="title-light">The Lantern </span><span class="title-red">Ledger Method</span></div>
    <div class="spine-author">HOLLIS PENWARDEN</div>
  </section>

  <section class="front">
    <h1 class="title">
      <div class="title-light">The Lantern</div>
      <div class="title-red">Ledger</div>
      <div class="title-red">Method</div>
    </h1>
    <p class="tagline">MASTER YOUR BUSINESS, MASTER YOUR LIFE</p>
    <svg class="tagline-glow" width="400" height="10" viewBox="0 0 400 10" aria-hidden="true">
      <defs>
        <linearGradient id="glowLine" x1="0" x2="1">
          <stop offset="0" stop-color="#ec1f27" stop-opacity="0"/>
          <stop offset="0.5" stop-color="#ec1f27" stop-opacity="1"/>
          <stop offset="1" stop-color="#ec1f27" stop-opacity="0"/>
        </linearGradient>
      </defs>
      <rect x="0" y="3" width="400" height="4" fill="url(#glowLine)"/>
    </svg>
    <div class="author-band"></div>
    <p class="author-name">HOLLIS PENWARDEN</p>
  </section>
</main>
</body>
</html>
```